Love pets? Create a veterinary business card that aligns with our new revamped website.

Greetings! We are a five-doctor veterinary hospital that seeks your expertise in designing a new business card that harmonizes with our recently revitalized website: www.tqrn.net. The card should feature our logo, the five doctors, operating hours, contact information, and communicate our purpose and personality.

Contact Information for Business Card

TBA

```html
<!DOCTYPE html>
<html lang="en">
<head>
<meta charset="utf-8">
<title>Maple Hollow Veterinary Hospital – Business Card</title>
<link rel="stylesheet" href="https://fonts.googleapis.com/css2?family=Roboto:wght@400;500;700;900&family=Great+Vibes&display=swap">
<style>
  :root {
    --backdrop: #c9cac6;
    --card: #f0cdb1;
    --card-light: #f5d9c3;
    --green: #4b8b2f;
    --brown: #7d5d2a;
    --divider: #b08a5c;
  }
  * { box-sizing: border-box; margin: 0; padding: 0; }
  html, body {
    width: 1113px; height: 1200px; overflow: hidden;
    background: var(--backdrop);
    font-family: "Roboto", Arial, sans-serif;
  }
  .sheet {
    width: 1113px; height: 1200px;
    display: flex; flex-direction: column; align-items: center; justify-content: center;
    gap: 40px;
  }
  .card {
    position: relative;
    width: 920px; height: 526px;
    background: var(--card);
    overflow: hidden;
  }
  .card__pattern {
    position: absolute; inset: 0;
    background: radial-gradient(circle at 30% 30%, var(--card-light), var(--card) 70%);
  }
  .card__footer {
    position: absolute; left: 0; right: 0; bottom: 28px;
    text-align: center;
    color: var(--green);
    font-size: 19px; letter-spacing: 2.4px; line-height: 1.2;
  }
  /* Brand */
  .brand {
    position: absolute; display: flex; align-items: center; gap: 22px;
    color: var(--green); font-weight: 700;
  }
  .brand__dot { flex: none; border-radius: 50%; background: var(--green); }
  .card--front .brand { left: 90px; top: 195px; }
  .card--front .brand__dot { width: 120px; height: 120px; }
  .card--front .brand__name { font-size: 60px; line-height: 1.05; }
  .card--front .brand__name small { display: block; font-size: 32px; letter-spacing: 1px; }
  .card--back .brand { left: 74px; top: 58px; gap: 12px; }
  .card--back .brand__dot { width: 46px; height: 46px; }
  .card--back .brand__name { font-size: 26px; line-height: 1.05; }
  .card--back .brand__name small { display: block; font-size: 14px; letter-spacing: .5px; }
  .tagline {
    position: absolute; right: 86px; top: 74px;
    font-family: "Great Vibes", cursive;
    font-size: 28px; color: var(--green);
  }
  /* Person */
  .person { position: absolute; left: 74px; top: 215px; }
  .person__name {
    font-size: 66px; font-weight: 900; color: var(--green);
    font-variant: small-caps; letter-spacing: 1px; line-height: 1;
  }
  .person__title { font-size: 24px; color: var(--brown); margin-top: 8px; line-height: 1.2; }
  /* Contacts */
  .contacts {
    position: absolute; left: 74px; top: 340px;
    display: flex;
  }
  .contacts__col { list-style: none; padding-right: 42px; }
  .contacts__col + .contacts__col { border-left: 1px solid var(--divider); padding-left: 42px; }
  .contacts__head { font-size: 13px; font-weight: 700; color: var(--green); line-height: 16px; margin-bottom: 4px; }
  .contacts__item {
    display: flex; align-items: center; gap: 10px;
    font-size: 18px; color: var(--brown); line-height: 27px;
  }
  .contacts__item svg { width: 16px; height: 16px; flex: none; fill: none; stroke: var(--green); stroke-width: 1.6; }
  .contacts__col--own { padding-top: 20px; }
</style>
</head>
<body>
<main class="sheet">
  <section class="card card--front">
    <div class="card__pattern" role="img" aria-label="Scattered dog-bone pattern in light peach"></div>
    <div class="brand">
      <span class="brand__dot"></span>
      <span class="brand__name">Maple Hollow<small>Veterinary Hospital</small></span>
    </div>
    <p class="card__footer">www.tqrn.net - Mon-Friday 8-7, Sat 9-1, Sun Closed</p>
  </section>

  <section class="card card--back">
    <div class="card__pattern" role="img" aria-label="Scattered dog-bone pattern in light peach"></div>
    <div class="brand">
      <span class="brand__dot"></span>
      <span class="brand__name">Maple Hollow<small>Veterinary Hospital</small></span>
    </div>
    <p class="tagline">Care Beyond the Clinic</p>
    <div class="person">
      <h1 class="person__name">Dr. Lena Marsh</h1>
      <p class="person__title">Doctor of Veterinary Medicine</p>
    </div>
    <div class="contacts">
      <ul class="contacts__col contacts__col--own">
        <li class="contacts__item"><svg viewBox="0 0 16 16"><rect x="4" y="1" width="8" height="14" rx="1.5"/><path d="M7 12.5h2"/></svg>(555) XXX-XXXX</li>
        <li class="contacts__item"><svg viewBox="0 0 16 16"><path d="M2 5q6-4 12 0v2h-3V5.5h-6V7H2z"/><rect x="3" y="8" width="10" height="6" rx="1"/></svg>(555) 214-0100</li>
        <li class="contacts__item"><svg viewBox="0 0 16 16"><rect x="1.5" y="3.5" width="13" height="9"/><path d="M1.5 3.5l6.5 5 6.5-5"/></svg>l.marsh@tqrn.net</li>
      </ul>
      <ul class="contacts__col">
        <li class="contacts__head">HOSPITAL</li>
        <li class="contacts__item"><svg viewBox="0 0 16 16"><rect x="4" y="1" width="8" height="14" rx="1.5"/><path d="M7 12.5h2"/></svg>(555) 214-0187</li>
        <li class="contacts__item"><svg viewBox="0 0 16 16"><path d="M2 5q6-4 12 0v2h-3V5.5h-6V7H2z"/><rect x="3" y="8" width="10" height="6" rx="1"/></svg>(555) 214-0100</li>
        <li class="contacts__item"><svg viewBox="0 0 16 16"><rect x="1.5" y="3.5" width="13" height="9"/><path d="M1.5 3.5l6.5 5 6.5-5"/></svg>info@tqrn.net</li>
      </ul>
    </div>
    <p class="card__footer">www.tqrn.net - Mon-Friday 8-7, Sat 9-1, Sun Closed</p>
  </section>
</main>
</body>
</html>
```